Anzeigengestaltung für Gebäudedienstleistungsunternehmen
Zielgruppe
Wir sind ein lokales Gebäudedienstleistungsunternehmen und bieten Gebäudereinigung und Haushaltsreinigung, Grünanlagenpflege und Gartenpflege, Winterdienst und Hausmeisterservice für Privat- und Gewerbekunden an.
Aufgabenstellung
Zur Info: Wir benötigen auch ein Flyerdesign. Dieses möchten wir in Anschluss an diesen Auftrag als 1-zu-1 Projekt an den Designer unserer Anzeige vergeben.
Diese Anzeige soll in dem lokalen Mitteilungsblatt (https://www.ortsbote-velun.com/index.php) erscheinen.
Es ist eine farbige zweispaltige (92mm) Anzeige mit der Höhe von 50mm.
Unser Logo und die Firmenfarben sollen verwendet werden. Gerne darf auch ein Foto benutzt werden (z.B. im Hintergrund), welches nach den Jahreszeiten gewechselt werden kann. Zum Beispiel: Frühjahr -> Gartenpflege, Sommer -> Gebäudereinigung, Herbst -> Winterdienst und im Winter -> Hausmeisterservice.
Der Text sollte unsere Dienstleistungen enthalten. Diese sind: Gebäude- und Haushaltsreinigung, Grünanlagen- und Gartenpflege, Winterdienst und Hausmeisterservice. Zusätzlich der Hinweis, dass wir sowohl Privat als auch Gewerbekunden ansprechen möchten.
Unsere Kontaktdaten sollen auch enthalten sein:
Internet: www.brimato.de, Telefon: 09471/3582140, E-Mail: kontakt@brimato.de
Falls es noch Platz gibt, dann wäre es schön noch den lokalen Bezug herzustellen, indem man die Postleitzahl und den Ort unserer Firma nennt. Eine Nennung der Straße ist nicht vorgesehen.
PLZ: 91207 Ort: Lauf an der Pegnitz od. Lauf a.d. Pegnitz

```html
<!DOCTYPE html>
<html lang="de">
<head>
<meta charset="utf-8">
<title>Anzeige Brimato Gebäudedienste</title>
<link href="https://fonts.googleapis.com/css2?family=Poppins:wght@800&family=Roboto:wght@300;400;500&family=Roboto+Condensed:wght@500;700&display=swap" rel="stylesheet">
<style>
  :root {
    --brand-blue: #0570a8;
    --tint-blue: rgba(30, 115, 165, 0.82);
    --white: #ffffff;
    --page: #ffffff;
  }
  * { box-sizing: border-box; margin: 0; padding: 0; }
  html, body {
    width: 1166px; height: 1200px; overflow: hidden;
    background: var(--page);
  }
  .ad {
    position: absolute; left: 33px; top: 300px;
    width: 1100px; height: 599px;
    overflow: hidden; color: var(--white);
  }
  .ad__photo {
    position: absolute; left: 0; top: 0; width: 1100px; height: 490px;
    background:
      radial-gradient(ellipse 260px 220px at 560px 420px, rgba(230,110,30,0.85), transparent 70%),
      radial-gradient(ellipse 300px 200px at 800px 380px, rgba(210,150,70,0.7), transparent 70%),
      linear-gradient(180deg, #3e3e1e 0%, #5a4a1c 35%, #6e5624 60%, #4f5a2a 100%);
  }
  .ad__tint { position: absolute; left: 0; top: 0; width: 1100px; height: 490px; }
  .ad__headline {
    position: absolute; left: 18px; top: 22px;
    font-family: "Poppins", sans-serif; font-weight: 800;
    font-size: 54px; letter-spacing: -0.8px; line-height: 1; white-space: nowrap;
  }
  .ad__copy {
    position: absolute; left: 22px; top: 117px;
    font-family: "Roboto", sans-serif; font-size: 33px; line-height: 40.5px;
  }
  .ad__copy .strong { font-weight: 500; }
  .ad__copy .light { font-weight: 300; }
  .ad__copy .audience { font-weight: 500; margin-top: 7px; }
  .ad__contact {
    position: absolute; left: 780px; top: 216px;
    font-family: "Roboto", sans-serif;
  }
  .ad__call { font-size: 30px; font-weight: 400; line-height: 36px; }
  .ad__phone {
    font-family: "Roboto Condensed", sans-serif; font-weight: 700;
    font-size: 45px; line-height: 1.1; margin-top: 8px; white-space: nowrap;
  }
  .ad__mail {
    font-family: "Roboto Condensed", sans-serif; font-weight: 500;
    font-size: 37px; line-height: 1.1; margin-top: 14px; white-space: nowrap;
  }
  .ad__band {
    position: absolute; left: 0; top: 490px; width: 1100px; height: 109px;
    background: var(--brand-blue);
  }
  .ad__web {
    position: absolute; left: 31px; top: 32px;
    font-family: "Roboto", sans-serif; font-size: 37px; font-weight: 400;
  }
  .ad__brand {
    position: absolute; right: 24px; top: 22px;
    display: flex; align-items: center; gap: 16px;
  }
  .ad__brand-mark { width: 56px; height: 56px; background: var(--white); }
  .ad__brand-name {
    font-family: "Roboto", sans-serif; font-weight: 500;
    font-size: 33px; line-height: 33px; text-transform: uppercase; letter-spacing: 0.5px;
  }
</style>
</head>
<body>
  <div class="ad">
    <div class="ad__photo" role="img" aria-label="Hintergrundfoto: hohe Gräser und Bäume im warmen Abendlicht"></div>
    <svg class="ad__tint" viewBox="0 0 1100 490" aria-hidden="true">
      <polygon points="0,0 683,0 534,490 0,490" fill="var(--tint-blue)"/>
      <polygon points="683,0 858,0 709,490 534,490" fill="rgba(40,110,150,0.18)"/>
    </svg>

    <h1 class="ad__headline">Der Rasen mäht sich nicht von alleine!</h1>

    <div class="ad__copy">
      <p class="strong">Stimmt! Das übernehmen wir!</p>
      <p class="strong">Wir kümmern uns um Ihre Immobilie!</p>
      <p class="light">Nutzen Sie unseren full-service rund<br>um Gebäude- und Haushaltsreinigung,<br>Grünanlagen- und Gartenpflege,<br>Winterdienst und Hausmeisterservice.</p>
      <p class="audience">Für Privat- und Gewerbekunden!</p>
    </div>

    <div class="ad__contact">
      <p class="ad__call">RUFEN SIE UNS<br>GERNE AN!</p>
      <p class="ad__phone">09471 358 2140</p>
      <p class="ad__mail">kontakt@brimato.de</p>
    </div>

    <div class="ad__band">
      <p class="ad__web">www.brimato.de</p>
      <div class="ad__brand">
        <span class="ad__brand-mark"></span>
        <p class="ad__brand-name">Brimato<br>Gebäudedienste</p>
      </div>
    </div>
  </div>
</body>
</html>
```